Está é a segunda experiência que tenho com site. Notei que na vês passada, comprando o mesmo pacotes, obtive no mínimo o dobro de projetos para escolher. Tento que para escolha de nome, não escolhi nenhum sugerido. São críticas, construtivas.

```html
<!DOCTYPE html>
<html lang="pt-BR">
<head>
<meta charset="utf-8">
<title>Vantora — Papel timbrado</title>
<link rel="stylesheet" href="https://fonts.googleapis.com/css2?family=Nunito:wght@400;700&display=swap">
<style>
  :root {
    --backdrop: #e9eaea;
    --paper: #ffffff;
    --teal: #1fb0b4;
    --teal-faint: #eaf6f7;
    --ink-soft: #6f7c7e;
  }
  * { box-sizing: border-box; margin: 0; padding: 0; }
  html, body {
    width: 1200px; height: 1200px; overflow: hidden;
    background: var(--backdrop);
    font-family: "Nunito", sans-serif;
  }
  .letterhead {
    position: absolute; left: 211px; top: 50px;
    width: 778px; height: 1100px;
    background: var(--paper);
    box-shadow: 0 6px 24px rgba(0,0,0,0.12);
    overflow: hidden;
  }
  .top-band {
    position: absolute; top: 0; right: 0;
    width: 230px; height: 14px;
    background: var(--teal);
  }
  .brand {
    position: absolute; top: 70px; right: 70px;
    text-align: right;
  }
  .brand-row { display: flex; align-items: center; gap: 10px; justify-content: flex-end; }
  .brand-dot { width: 16px; height: 16px; border-radius: 50%; background: var(--teal); }
  .brand-name { font-size: 44px; font-weight: 700; color: var(--teal); line-height: 1; }
  .brand-tagline {
    margin-top: 6px; font-size: 13px; letter-spacing: 4px;
    color: var(--teal); text-transform: lowercase;
  }
  .watermark-area {
    position: absolute; left: 60px; top: 260px;
    width: 658px; height: 600px;
    background: linear-gradient(160deg, var(--teal-faint) 0%, var(--paper) 85%);
  }
  .footer-web {
    position: absolute; left: 60px; bottom: 90px;
    font-size: 12px; color: var(--ink-soft);
  }
  .footer-contact {
    position: absolute; left: 60px; bottom: 52px;
    font-size: 12px; color: var(--ink-soft); letter-spacing: 0.3px;
    white-space: nowrap;
  }
  .footer-contact span + span::before { content: "  |  "; white-space: pre; }
  .bottom-band {
    position: absolute; left: 0; bottom: 0;
    width: 270px; height: 14px; background: var(--teal);
  }
  .bottom-line {
    position: absolute; left: 270px; bottom: 0;
    width: 508px; height: 3px; background: var(--teal);
  }
</style>
</head>
<body>
  <main class="letterhead">
    <div class="top-band"></div>
    <header class="brand">
      <div class="brand-row">
        <span class="brand-dot"></span>
        <span class="brand-name">Vantora</span>
      </div>
      <div class="brand-tagline">saúde integrada</div>
    </header>
    <div class="watermark-area" role="img" aria-label="Área reservada para marca d'água da empresa em tom suave"></div>
    <p class="footer-web">www.vantoramed.com.br</p>
    <p class="footer-contact">
      <span>Rua das Acácias, 120, Centro, São Paulo, SP</span><span>Tel. (11) 4000-1234</span><span>contato@vantoramed.com.br</span>
    </p>
    <div class="bottom-band"></div>
    <div class="bottom-line"></div>
  </main>
</body>
</html>
```